Looking to design a new sign for our church.

Looking for a new sign
4 x 8 feet dimension
We are renaming the church "Keller Ridge Community Church"
looking for legible graphics
Would like some type of backdrop being a family tree (oak) / open to other ideas as you are led
I have included a pic of the old sign for your review
would like to incorporate our ministry logo on the lower right hand corner of the sign / see file attached

```html
<!DOCTYPE html>
<html lang="en">
<head>
<meta charset="UTF-8">
<title>Keller Ridge Community Church – Sign</title>
<link href="https://fonts.googleapis.com/css2?family=Cinzel:wght@400&family=Montserrat:wght@600&display=swap" rel="stylesheet">
<style>
  :root {
    --backdrop: #c8c8c8;
    --navy-deep: #00173a;
    --navy: #011b45;
    --gold: #d6ae68;
    --gold-edge: #c8934a;
    --gold-light: #efcd8f;
    --white: #ffffff;
    --ink: #0c1e3d;
  }
  html, body {
    margin: 0;
    width: 1200px;
    height: 1200px;
    overflow: hidden;
    background: var(--backdrop);
  }
  .sign {
    position: absolute;
    left: 42px;
    top: 298px;
    width: 1116px;
    height: 599px;
    background: linear-gradient(120deg, var(--navy-deep), var(--navy));
    overflow: hidden;
  }
  .ministry-mark {
    position: absolute;
    left: 0;
    right: 0;
    top: 52px;
    margin: 0;
    text-align: center;
    font-family: "Cinzel", serif;
    font-weight: 400;
    font-size: 26px;
    letter-spacing: 6px;
    line-height: 1;
    color: var(--gold);
  }
  .ministry-emblem {
    position: absolute;
    left: 507px;
    top: 234px;
    width: 106px;
    height: 106px;
    border-radius: 50%;
    background: radial-gradient(circle at 40% 35%, var(--gold-light), var(--gold-edge));
  }
  .church-name {
    position: absolute;
    top: 266px;
    margin: 0;
    font-family: "Cinzel", serif;
    font-weight: 400;
    font-size: 78px;
    letter-spacing: 3px;
    line-height: 1;
    color: var(--white);
    white-space: nowrap;
  }
  .church-name--left { right: 638px; }
  .church-name--right { left: 636px; }
  .church-tagline {
    position: absolute;
    left: 0;
    right: 0;
    top: 368px;
    margin: 0;
    display: flex;
    justify-content: center;
    align-items: center;
    gap: 20px;
    font-family: "Cinzel", serif;
    font-weight: 400;
    font-size: 54px;
    letter-spacing: 4px;
    line-height: 1;
    color: var(--gold);
    white-space: nowrap;
  }
  .tagline-dot {
    width: 14px;
    height: 14px;
    border-radius: 50%;
    background: var(--gold);
  }
  .gold-rule {
    position: absolute;
    left: 0;
    right: 0;
    top: 468px;
    height: 5px;
    background: linear-gradient(90deg, var(--gold-edge), var(--gold-light) 50%, var(--gold-edge));
  }
  .schedule-band {
    position: absolute;
    left: 0;
    right: 0;
    top: 485px;
    bottom: 0;
    background: linear-gradient(90deg, var(--gold-edge) 18%, var(--gold-light) 45%, var(--gold-light) 55%, var(--gold-edge) 78%);
  }
  .schedule-list {
    position: absolute;
    top: 16px;
    margin: 0;
    padding: 0;
    list-style: none;
    font-family: "Montserrat", sans-serif;
    font-weight: 600;
    font-size: 25px;
    line-height: 31px;
    letter-spacing: 0.5px;
    color: var(--ink);
  }
  .schedule-list--times { left: 289px; }
  .schedule-list--events { left: 546px; }
  .schedule-divider {
    position: absolute;
    left: 481px;
    top: 16px;
    width: 2px;
    height: 86px;
    background: var(--ink);
  }
</style>
</head>
<body>
  <div class="sign">
    <p class="ministry-mark">KELLER RIDGE</p>
    <div class="ministry-emblem" role="img" aria-label="Ministry emblem placeholder"></div>
    <h1 class="church-name church-name--left">KELLER</h1>
    <span class="church-name church-name--right">RIDGE</span>
    <p class="church-tagline"><span class="tagline-dot"></span>COMMUNITY CHURCH<span class="tagline-dot"></span></p>
    <div class="gold-rule"></div>
    <div class="schedule-band">
      <ul class="schedule-list schedule-list--times">
        <li>10:30 AM</li>
        <li>9:30 AM</li>
        <li>6:00 PM</li>
      </ul>
      <div class="schedule-divider"></div>
      <ul class="schedule-list schedule-list--events">
        <li>WORSHIP SERVICE</li>
        <li>SUNDAY SCHOOL</li>
        <li>WEDNESDAY SERVICE</li>
      </ul>
    </div>
  </div>
</body>
</html>
```